Calloway Aeronautics website

We are an aviation company based in Miramar, FL but with worldwide coverage. We are involved in commercial aircraft (mostly freighters) trading, sale & leasing. Specifically, we specialized in freighters of the Vantrex family (V310, V320, V330, V340, V350). We also assist with financing, sale/leaseback. Handle special aviation projects and provide consultancy services. Currently engaged in a Vantrex 350 passenger to Freighter conversion (P2F).

Website Preliminary Initial Content/Sections as follows:

About Us
Founded in 2011, Calloway Aeronautics' management has many years of experience in Aviation, a strong background in scheduled airlines with emphasis in all cargo operations, freight forwarding supply chain and freight logistics, as well as ACMI and CMI operations.

Calloway’s focuses in facilitating wet and dry lease operations, charter and ACMI programs consultancy, aircraft sales, leasing and procurement, aviation consultancy and aircraft management.

Calloway team is a hands-on reliable alternative that works toward achieving your aircraft and aviation objectives by meeting your requirements and timeframe throughout professional and personalized service.

Teodoro Lasalle has over three decades of experience in the aviation field including aircraft maintenance, airline management, supply chain and logistics management. Teodoro is a true entrepreneur with proven experience and expertise on the multiple facets of the commercial aviation industry throughout the creation and development of a cluster of aviation entities. Teodoro is the founder and former sole member/chairman of 64 Jet, a Vantrex 340 All-Cargo U.S. Certificated Air Carrier created from scratch in 2014 which nowadays conforms a superb growing airline platform with an immaculate compliance operational record.

Services

Aircraft Finance, Trading, Procurement and Leasing
Calloway buys, sells, leases and facilitates aircraft trading while specializes in structured aircraft investment projects. Calloway has deep industry relationships and years of expertise, allowing to successfully execute lease transactions. We assist airlines, financial institutions and leasing companies when selling or purchasing aircraft.

Aircraft Available for Sale/Lease

Sale/Leaseback
Sale-leaseback is a method of financing. If your company needs liquidity, your aircraft or engine can serve as collateral for a loan throughout a sale-leaseback transaction. Sale-leaseback can free the equity tied up in aircraft or asset. Even if there is no pressing need for funds, a sale-leaseback allows you to use the equity tied up in your aircraft in a more productive fashion. Leaseback arrangements are usually employed because they confer financing, accounting or taxation benefits.

Passenger to Freighter Conversion (P2F)
Pandemic has seen the resurgence of operators packing freight into the main cabins of passenger aircraft. Carriers have been allowed to transport cargo in the cabin by removing passenger seats completely. NCA/ORSA have established exemptions that allow operators to fly in “Preighter” configuration for a limited time. Calloway is closely working with a U.S. group that is developing a Class E Supplemental Type Certificate (STC) for applicability on V350 aircraft which will include a cargo door for containerized freight. Final approvals are expected during first quarter of 2022.
Wet lease
Throughout our deep relationships within the industry, Calloway facilitates short or long-term wet leases to airlines and qualified parties around the globe, whereby we provide the Aircraft, Crews, Maintenance and Insurance (ACMI) worldwide services at competitive rates. We also specialize in AM leases where the aircraft is registered onto Lessee´s AOC with all maintenance services included in the rates, covering all maintenance risks, or CM or CMI where the client provides the aircraft.

Dry Lease
We offer aircraft from our own portfolio on dry lease or could engage in procuring the aircraft of your choice.

Asset & Aircraft Management
We provide aircraft owners Aircraft Management services, where we manage the technical side of the aircraft or the asset. Calloway also provides Harwick Dynamo engines trading, repair and full management services. We also buy Vantrex/Skylane surplus inventory.

Worldwide Charters
We facilitate the arrangement of full charters to airlines and logistics companies. Certain territory restrictions may apply.

Aviation Consultancy
We provide airline consultancy services for new or special projects. Calloway also specializes on All Cargo International route analysis, implementation and development. Our team provides professional guidance in obtaining worldwide both scheduled and charter authority.

Target Market(s)

Our target market are the airlines, logistics companies and commercial aviation related entities

Industry/Entity Type

Commercial Aviation

Coding

Number of Pages Required

3 page

Requirements
Must have
• Illustrations of wide body freighters such V350, V340, V320

```html
<!DOCTYPE html>
<html lang="en">
<head>
<meta charset="utf-8">
<title>Calloway Aeronautics</title>
<link href="https://fonts.googleapis.com/css2?family=Poppins:ital,wght@0,400;0,500;0,600;0,700;0,800;1,800&display=swap" rel="stylesheet">
<style>
:root{
  --navy:#0b1546;
  --navy-deep:#08113a;
  --steel:#8c9db0;
  --steel-light:#b9c4d0;
  --mist:#e9edf2;
  --text:#4a4f5e;
  --white:#ffffff;
  --line:#e2e5ea;
}
*{margin:0;padding:0;box-sizing:border-box}
html,body{width:1200px;height:4494px;overflow:hidden;background:var(--white)}
body{position:relative;font-family:'Poppins',sans-serif;color:var(--text)}
.abs{position:absolute}
.shapes{position:absolute;left:0;top:0;width:1200px;height:4494px}

/* header */
.logo{position:absolute;color:var(--white);text-align:center;font-weight:400;letter-spacing:1px;line-height:1}
.logo .name{display:block;font-size:30px}
.logo .sub{display:block;font-size:13px;letter-spacing:11px;margin-top:6px}
.nav{position:absolute;left:466px;top:46px;display:flex;gap:28px;font-size:13px;font-weight:500;color:var(--white)}
.search{position:absolute;left:932px;top:42px}
.btn-touch{position:absolute;left:980px;top:38px;width:131px;height:34px;background:var(--white);color:var(--navy);font-size:12px;font-weight:600;display:flex;align-items:center;justify-content:center}
.head-rule{position:absolute;left:90px;top:106px;width:1021px;height:1px;background:rgba(255,255,255,.15)}

.hero-title{position:absolute;left:0;width:1200px;text-align:center;font-weight:700;line-height:1;letter-spacing:1px}
.hero-title.l1{top:192px;font-size:84px;color:var(--white)}
.hero-title.l2{top:270px;font-size:78px;color:var(--steel)}
.hero-sub{position:absolute;left:0;width:1200px;top:360px;text-align:center;color:var(--white);font-size:20px;font-weight:400}
.scroll{position:absolute;left:90px;top:400px;color:var(--white);font-size:10px;transform:rotate(-90deg);transform-origin:left top;top:440px}
.slide-no{position:absolute;left:1024px;top:422px;color:var(--white);font-size:42px;font-weight:600}
.slide-no small{font-size:18px;font-weight:400;margin-left:4px}
.photo{position:absolute}

/* section titles */
.sec-title{position:absolute;color:var(--navy);font-weight:700;font-size:44px;line-height:1.1}
.p{position:absolute;font-size:13.5px;line-height:23.4px;color:var(--text)}
.btn-dark{position:absolute;background:var(--navy);color:var(--white);font-size:11.5px;font-weight:600;display:flex;align-items:center;justify-content:center}

/* services tabs */
.tab{position:absolute;top:1508px;width:180px;margin-left:-90px;text-align:center;color:var(--navy);font-size:10.5px;line-height:15px;font-weight:500}
.tab svg{display:block;margin:0 auto 14px}

/* detail */
.dots{position:absolute;left:300px;top:1688px;display:grid;grid-template-columns:repeat(3,8px);gap:17px 18px}
.dots i{width:8px;height:8px;border-radius:50%;background:#d3d8df}
.detail-h{position:absolute;left:90px;top:1834px;font-size:22px;font-weight:700;color:var(--navy)}
.detail-s{position:absolute;left:90px;top:1866px;font-size:13px;font-weight:700;color:var(--navy)}

/* stats */
.stat{position:absolute;top:2360px;width:220px;margin-left:-110px;text-align:center;color:var(--white)}
.stat .num{font-size:64px;font-weight:800;font-style:italic;line-height:1;margin-top:10px;letter-spacing:-2px}
.stat .lbl{font-size:16px;font-weight:400;margin-top:10px}

/* faq */
.faq-bg{position:absolute;left:150px;top:3190px;font-size:190px;font-weight:800;color:#ececec;transform:rotate(-90deg);transform-origin:left top;line-height:1;letter-spacing:6px}
.faq-item{position:absolute;left:616px;width:397px;height:47px;background:var(--white);box-shadow:0 4px 14px rgba(10,20,60,.12);display:flex;align-items:center;justify-content:space-between;padding:0 20px;font-size:12px;font-weight:500;color:var(--navy)}
.faq-item b{font-size:18px;font-weight:500}

/* blog */
.card{position:absolute;top:3371px;width:282px;height:370px;background:var(--white);box-shadow:0 6px 20px rgba(10,20,60,.1)}
.card .img{height:210px}
.card .meta{margin:30px 0 0 28px;font-size:11px;color:var(--navy)}
.card h3{margin:12px 28px 0;font-size:13px;font-weight:700;color:var(--navy);line-height:20px}
.card p{margin:10px 28px 0;font-size:11.5px;line-height:18px;color:var(--text)}

/* newsletter */
.news-input{position:absolute;left:279px;top:4029px;width:642px;height:57px;background:var(--white);display:flex;align-items:center}
.news-input span{margin-left:52px;font-size:15px;color:#7a8090}
.news-btn{position:absolute;right:4px;top:4px;bottom:4px;width:144px;background:var(--steel);color:var(--white);font-size:15px;font-weight:700;display:flex;align-items:center;justify-content:center}

/* footer */
.f-h{position:absolute;color:var(--white);font-size:17px;font-weight:700}
.f-list{position:absolute;list-style:none;color:var(--white);font-size:13px;line-height:26.5px}
.f-c{position:absolute;left:866px;color:var(--white);font-size:13px;line-height:19px}
.f-c b{font-size:12px;font-weight:600;display:block}
.social{position:absolute;top:4297px;width:36px;height:36px;border-radius:50%;border:1px solid rgba(255,255,255,.35)}
.copy{position:absolute;left:0;top:4458px;width:1200px;text-align:center;color:var(--white);font-size:11px}
.to-top{position:absolute;left:1136px;top:4422px;width:40px;height:40px;border-radius:50%;background:var(--white);display:flex;align-items:center;justify-content:center}
</style>
</head>
<body>

<svg width="0" height="0" style="position:absolute">
  <symbol id="plane" viewBox="0 0 40 40">
    <path d="M20 3c1.6 0 2.4 2 2.4 4v7l13 7v3.5l-13-3.5v8l4 3v3l-6.4-1.7-6.4 1.7v-3l4-3v-8l-13 3.5v-3.5l13-7v-7c0-2 .8-4 2.4-4z" fill="none" stroke="currentColor" stroke-width="1.6" stroke-linejoin="round"/>
  </symbol>
</svg>

<!-- background shapes -->
<svg class="shapes" viewBox="0 0 1200 4494" aria-hidden="true">
  <defs>
    <linearGradient id="heroGrad" x1="0" y1="0" x2="0" y2="1">
      <stop offset="0" stop-color="#0a1342"/><stop offset="1" stop-color="#1b2759"/>
    </linearGradient>
    <linearGradient id="statGrad" x1="0" y1="0" x2="0" y2="1">
      <stop offset="0" stop-color="#7f91a6"/><stop offset="1" stop-color="#b7c3cf"/>
    </linearGradient>
    <linearGradient id="newsGrad" x1="0" y1="0" x2="0" y2="1">
      <stop offset="0" stop-color="#0b1546"/><stop offset="1" stop-color="#08113a"/>
    </linearGradient>
  </defs>
  <polygon points="0,0 1200,0 1200,540 600,470 0,540" fill="url(#heroGrad)"/>
  <polygon points="0,640 640,1099 0,1540" fill="#e3e8ee"/>
  <polygon points="0,2363 1200,2136 1200,2625 0,2625" fill="url(#statGrad)"/>
  <polygon points="0,3994 600,3837 1200,4010 1200,4494 0,4494" fill="var(--steel-light)"/>
  <polygon points="0,4004 600,3865 1200,4020 1200,4494 0,4494" fill="url(#newsGrad)"/>
  <line x1="90" y1="4442" x2="1111" y2="4442" stroke="rgba(255,255,255,.15)"/>
</svg>

<!-- header -->
<div class="logo" style="left:88px;top:24px"><span class="name">CALLOWAY</span><span class="sub">AERONAUTICS</span></div>
<nav class="nav"><span>HOME</span><span>ABOUT US</span><span>SERVICES</span><span>FREIGHTERS</span><span>CONTACT US</span></nav>
<svg class="search" width="24" height="24" viewBox="0 0 24 24"><circle cx="10" cy="10" r="7" fill="none" stroke="#fff" stroke-width="2"/><line x1="15" y1="15" x2="21" y2="21" stroke="#fff" stroke-width="2"/></svg>
<div class="btn-touch">GET IN TOUCH</div>
<div class="head-rule"></div>

<!-- hero -->
<div class="hero-title l1">CALLOWAY</div>
<div class="hero-title l2">AERONAUTICS</div>
<div class="hero-sub">WE ARE AN AVIATION COMPANY BASED IN MIRAMAR, FL</div>
<div class="scroll">SCROLL</div>
<svg class="abs" style="left:92px;top:450px" width="18" height="50" viewBox="0 0 18 50"><path d="M2 2h14L9 12z M2 17h14L9 27z M2 32h14L9 42z" fill="#fff"/><path d="M2 40h14L9 50z" fill="none" stroke="#fff"/></svg>
<div class="slide-no">01/<small>03</small></div>
<div class="photo" role="img" aria-label="Wide-body freighter aircraft seen from the front" style="left:52px;top:462px;width:1090px;height:305px;background:radial-gradient(ellipse at 50% 55%,#f4f5f7 0%,#d9dde3 45%,rgba(255,255,255,0) 72%)"></div>

<!-- about -->
<div class="photo" role="img" aria-label="Freighter aircraft taking off at sunset" style="left:0;top:698px;width:602px;height:802px;clip-path:polygon(0 0,100% 50%,0 100%);background:linear-gradient(180deg,#8fa9c2 0%,#c9b7ab 55%,#3b4150 100%)"></div>
<h2 class="sec-title" style="left:685px;top:915px">ABOUT US</h2>
<p class="p" style="left:685px;top:990px;width:426px">Founded in 2011, Calloway Aeronautics' management has many years of experience in Aviation, a strong background in scheduled airlines with emphasis in all cargo operations, freight forwarding supply chain and freight logistics, as well as ACMI and CMI operations.</p>
<p class="p" style="left:685px;top:1119px;width:426px">Calloway’s focuses in facilitating wet &amp; dry lease operations, charter and ACMI programs consultancy, aircraft sales, leasing and procurement, aviation consultancy and aircraft management.</p>
<div class="btn-dark" style="left:685px;top:1238px;width:123px;height:35px">LEARN MORE</div>

<!-- services -->
<h2 class="sec-title" style="left:0;width:1200px;text-align:center;top:1403px">OUR SERVICES</h2>
<div class="abs" style="left:580px;top:1462px;width:40px;height:2px;background:var(--line)"></div>
<div class="tab" style="left:174px"><svg width="34" height="34" style="color:var(--navy)"><use href="#plane"/></svg>AIRCRAFT FINANCE, TRADING,<br>PROCUREMENT AND LEASING</div>
<div class="tab" style="left:349px"><svg width="34" height="34" style="color:var(--navy)"><use href="#plane"/></svg>CALLOWAY<br>DRY LEASE</div>
<div class="tab" style="left:471px"><svg width="34" height="34" style="color:var(--navy)"><use href="#plane"/></svg>WORLDWIDE<br>CHARTERS</div>
<div class="tab" style="left:621px"><svg width="34" height="34" style="color:var(--navy)"><use href="#plane"/></svg>AIRCRAFT AVAILABLE<br>FOR SALE/LEASE</div>
<div class="tab" style="left:762px"><svg width="34" height="34" style="color:var(--navy)"><use href="#plane"/></svg>CALLOWAY<br>WET LEASE</div>
<div class="tab" style="left:917px"><svg width="34" height="34" style="color:var(--navy)"><use href="#plane"/></svg>PASSENGER TO FREIGHTER<br>CONVERSION (P2F)</div>
<div class="tab" style="left:1066px"><svg width="34" height="34" style="color:var(--navy)"><use href="#plane"/></svg>AVIATION<br>CONSULTANCY</div>
<div class="abs" style="left:90px;top:1613px;width:1021px;height:1px;background:var(--line)"></div>
<div class="abs" style="left:560px;top:1612px;width:118px;height:3px;background:var(--navy)"></div>

<!-- service detail -->
<div class="photo" role="img" aria-label="Nose of a wide-body freighter on the apron at dusk" style="left:602px;top:1596px;width:598px;height:840px;clip-path:polygon(100% 0,0 50%,100% 100%);background:linear-gradient(160deg,#d9dde2 0%,#9aa0a6 45%,#4a3d2e 75%,#1f2230 100%)"></div>
<div class="dots"><i></i><i></i><i></i><i></i><i></i><i></i><i></i><i></i><i></i><i></i><i></i><i></i></div>
<svg class="abs" style="left:90px;top:1770px;color:var(--navy)" width="58" height="58"><use href="#plane"/></svg>
<h3 class="detail-h">AIRCRAFT AVAILABLE FOR SALE/LEASE</h3>
<div class="detail-s">SALE/LEASEBACK</div>
<p class="p" style="left:90px;top:1920px;width:425px;font-size:13.6px;line-height:23.2px">Sale-leaseback is a method of financing. If your company needs liquidity, your aircraft or engine can serve as collateral for a loan throughout a sale-leaseback transaction. Sale-leaseback can free the equity tied up in aircraft or asset. Even if there is no pressing need for funds, a sale-leaseback allows you to use the equity tied up in your aircraft in a more productive fashion. Leaseback arrangements are usually employed because they confer financing, accounting or taxation benefits.</p>

<!-- stats -->
<div class="stat" style="left:258px">
  <svg width="54" height="60" viewBox="0 0 54 60" fill="none" stroke="#fff" stroke-width="2"><rect x="3" y="8" width="48" height="48" rx="3"/><line x1="3" y1="20" x2="51" y2="20"/><line x1="15" y1="2" x2="15" y2="12"/><line x1="39" y1="2" x2="39" y2="12"/><path d="M12 30h6M24 30h6M36 30h6M12 40h6M24 40h6M36 40h6" /></svg>
  <div class="num">15</div><div class="lbl">YEARS IN BUSINESS</div>
</div>
<div class="stat" style="left:487px">
  <svg width="60" height="60" viewBox="0 0 60 60" fill="none" stroke="#fff" stroke-width="2"><circle cx="30" cy="18" r="11"/><path d="M8 58c0-14 10-22 22-22s22 8 22 22z"/><path d="M27 36l3 12 3-12"/></svg>
  <div class="num">10</div><div class="lbl">OUR PROFESSIONALS</div>
</div>
<div class="stat" style="left:715px">
  <svg width="70" height="60" viewBox="0 0 70 60" fill="none" stroke="#fff" stroke-width="2"><path d="M12 3l2.5 5 5.5.8-4 3.9 1 5.5-5-2.6-5 2.6 1-5.5-4-3.9 5.5-.8z M35 1l2.5 5 5.5.8-4 3.9 1 5.5-5-2.6-5 2.6 1-5.5-4-3.9 5.5-.8z M58 3l2.5 5 5.5.8-4 3.9 1 5.5-5-2.6-5 2.6 1-5.5-4-3.9 5.5-.8z"/><circle cx="33" cy="34" r="7"/><path d="M20 55c0-8 6-12 13-12s13 4 13 12"/><circle cx="47" cy="49" r="8"/><path d="M43 49l3 3 5-6"/></svg>
  <div class="num">05</div><div class="lbl">SATISFIED CUSTOMERS</div>
</div>
<div class="stat" style="left:944px">
  <svg width="70" height="60" viewBox="0 0 70 60" fill="none" stroke="#fff" stroke-width="2"><rect x="3" y="22" width="30" height="34" rx="2"/><rect x="38" y="30" width="28" height="26" rx="2"/><circle cx="36" cy="44" r="8"/><path d="M36 1v18M30 7l6-6 6 6M24 12v8M48 12v8"/></svg>
  <div class="num">100</div><div class="lbl">MANAGED DEVICES</div>
</div>

<!-- faq -->
<div class="faq-bg">FAQ</div>
<div class="photo" role="img" aria-label="Businessman in a suit standing inside a large question mark" style="left:314px;top:2694px;width:262px;height:506px;border-radius:130px 130px 20px 20px;background:linear-gradient(180deg,#e7e3df 0%,#2b3040 45%,#1c2131 100%)"></div>
<h2 class="sec-title" style="left:616px;top:2778px;font-size:44px;line-height:49px">FREQUENTLY ASKED<br>QUESTIONS</h2>
<div class="abs" style="left:616px;top:2890px;width:42px;height:2px;background:var(--line)"></div>
<div class="faq-item" style="top:2918px">Is anyone can register in the program ? <b>+</b></div>
<div class="faq-item" style="top:2974px">How we get the awrd ? <b>+</b></div>
<div class="faq-item" style="top:3030px">when it will be last day to submit a report ? <b>+</b></div>
<div class="faq-item" style="top:3085px">How we get the awrd ? <b>+</b></div>

<!-- blog -->
<h2 class="sec-title" style="left:0;width:1168px;text-align:center;top:3283px">LATEST BLOG</h2>
<article class="card" style="left:159px"><div class="img" role="img" aria-label="Freighter being loaded with cargo at the gate" style="background:linear-gradient(135deg,#6e7480,#c9ced6 55%,#8b5e3c)"></div><div class="meta">byJohn &nbsp;•&nbsp; January 2021</div><h3>SOME BLOG POST HEADING<br>GOES HERE WITH...</h3><p>Aenean sollicitudin, lorem quis auctor, nisi elit consequat ipsum nec...</p></article>
<article class="card" style="left:459px"><div class="img" role="img" aria-label="Business jet parked on the tarmac" style="background:linear-gradient(180deg,#b88a5e,#e3d6c7 50%,#8a8580)"></div><div class="meta">byJohn &nbsp;•&nbsp; January 2021</div><h3>SOME BLOG POST HEADING<br>GOES HERE WITH...</h3><p>Aenean sollicitudin, lorem quis auctor, nisi elit consequat ipsum nec...</p></article>
<article class="card" style="left:759px"><div class="img" role="img" aria-label="Jet engine and wing of a parked airliner" style="background:linear-gradient(180deg,#a9c0d6,#dfe5ea 55%,#7d858f)"></div><div class="meta">byJohn &nbsp;•&nbsp; January 2021</div><h3>SOME BLOG POST HEADING<br>GOES HERE WITH...</h3><p>Aenean sollicitudin, lorem quis auctor, nisi elit consequat ipsum nec...</p></article>

<!-- newsletter -->
<div class="photo" role="img" aria-label="Freighter aircraft climbing after take-off" style="left:0;top:3828px;width:288px;height:262px;clip-path:polygon(0 70%,100% 0,60% 55%,0 100%);background:linear-gradient(135deg,#f1f3f5,#b9c1cb)"></div>
<h2 class="sec-title" style="left:0;width:1200px;text-align:center;top:3956px;color:var(--white)">NEWSLETTER</h2>
<div class="news-input">
  <svg class="abs" style="left:30px;top:23px" width="16" height="12" viewBox="0 0 16 12"><rect x=".5" y=".5" width="15" height="11" fill="#b9c1cb"/><path d="M1 1l7 6 7-6" fill="none" stroke="#fff"/></svg>
  <span>Enter your email address</span>
  <div class="news-btn">SUBSCRIBE</div>
</div>

<!-- footer -->
<div class="logo" style="left:130px;top:4208px"><span class="name" style="font-size:29px">CALLOWAY</span><span class="sub" style="font-size:13px;letter-spacing:10px">AERONAUTICS</span></div>
<div class="social" style="left:181px"></div>
<div class="social" style="left:226px"></div>
<div class="social" style="left:272px"></div>
<div class="f-h" style="left:426px;top:4174px">QUICK LINKS</div>
<ul class="f-list" style="left:426px;top:4218px"><li>Home</li><li>Our Story</li><li>Freighters</li><li>Clients</li><li>News / Events</li></ul>
<div class="f-h" style="left:626px;top:4174px">INFORMATION</div>
<ul class="f-list" style="left:626px;top:4218px"><li>Important information</li><li>Disclosures</li><li>USA PATRIOT Act</li><li>Privacy and cookies</li><li>Sitemap</li></ul>
<div class="f-h" style="left:846px;top:4166px">CONTACT US</div>
<svg class="abs" style="left:846px;top:4223px" width="12" height="12" viewBox="0 0 12 12"><path d="M2 1l2.5 0 1 3-1.5 1a7 7 0 0 0 3 3l1-1.5 3 1v2.5c-6 .5-9.5-3-9-9z" fill="#fff"/></svg>
<div class="f-c" style="top:4219px"><b>Phone</b>+1 305 555 0142</div>
<svg class="abs" style="left:846px;top:4276px" width="12" height="9" viewBox="0 0 12 9"><rect width="12" height="9" fill="#fff"/><path d="M0 0l6 5 6-5" fill="none" stroke="#0b1546"/></svg>
<div class="f-c" style="top:4271px"><b>Email</b>info@callowayaero.test</div>
<svg class="abs" style="left:847px;top:4330px" width="10" height="13" viewBox="0 0 10 13"><path d="M5 13S0 7.5 0 5a5 5 0 0 1 10 0c0 2.5-5 8-5 8z" fill="#fff"/><circle cx="5" cy="5" r="1.8" fill="#0b1546"/></svg>
<div class="f-c" style="top:4327px"><b>Location</b>Some address line goes here<br>city name country</div>
<div class="copy">© COPYRIGHT 2021, CALLOWAY AERONAUTICSALL RIGHTS RESERVED</div>
<div class="to-top"><svg width="10" height="7" viewBox="0 0 10 7"><path d="M1 6l4-4 4 4" fill="none" stroke="#0b1546" stroke-width="2"/></svg></div>

</body>
</html>
```